Harbour Lantern Fliers and logo design

We need to design a product logo and some informational fliers for a summit quest.
I have attached our Harbour Lantern logo - colours need to be complimentary but not the same, we would like fresh, funky but still professional. We generally communicate in a fairly casual way to reach our market. (We don't like boring)
Clear and simple - not too busy
images are good but not actual photos
Here is our website to give you an idea www.harbourlantern-example.co.nz
The flier is a 3 page document.
The logo is to say Summit Quest. The challenge is based on exercise, connecting with people, giving, learning and taking notice (The 4 keys to brightwater) Once agin the logo needs to be complementary but not the same.
The Harbour lantern logo needs to be on the fliers but the summit quest logo is separate.
Thanks very much!!

```html
<!DOCTYPE html>
<html lang="en">
<head>
<meta charset="utf-8">
<title>10 Tips to Improve Your Wellbeing – Summit Quest</title>
<link href="https://fonts.googleapis.com/css2?family=Arimo:wght@400;700&display=swap" rel="stylesheet">
<style>
  :root {
    --teal: #06706a;
    --green: #9bc057;
    --orange: #e05a38;
    --brand-teal: #2fae96;
    --quest-green: #21a88f;
    --ink: #1d1d1b;
    --paper: #ffffff;
    --edge: #9a9a9a;
  }
  * { margin: 0; padding: 0; box-sizing: border-box; }
  html, body { width: 928px; height: 1200px; overflow: hidden; background: var(--paper); }
  body { font-family: "Arimo", Arial, sans-serif; color: var(--ink); }
  .sheet { position: relative; width: 928px; height: 1200px; border: 1px solid var(--edge); overflow: hidden; }
  .frame { position: absolute; inset: 0; }
  .quest-mark { position: absolute; left: 36px; top: 48px; display: flex; align-items: center; gap: 12px; }
  .quest-mark .dot { width: 52px; height: 52px; border-radius: 50%; background: var(--quest-green); }
  .quest-mark .name { font-weight: 700; font-size: 38px; color: var(--quest-green); letter-spacing: 1px; }
  .partner-mark { position: absolute; left: 610px; top: 70px; width: 230px; font-weight: 700; font-size: 34px; line-height: 34px; color: var(--brand-teal); }
  .title { position: absolute; left: 72px; top: 186px; color: var(--paper); font-weight: 700; }
  .title .big { display: block; font-size: 118px; line-height: 110px; letter-spacing: -1px; }
  .title .sub { display: block; font-size: 45px; line-height: 52px; margin-top: 10px; }
  .intro { position: absolute; left: 76px; top: 428px; width: 760px; font-size: 14px; line-height: 17.6px; }
  .intro p + p { margin-top: 17px; }
  .tip { position: absolute; left: 132px; width: 746px; font-size: 14px; line-height: 17.6px; }
  .tip strong { font-weight: 700; }
  .tip .num { position: absolute; left: -56px; top: -5px; width: 28px; height: 28px; border-radius: 50%;
    background: var(--orange); color: var(--paper); font-size: 13px; font-weight: 700; display: flex;
    align-items: center; justify-content: center; box-shadow: 0 0 0 2px var(--paper), 0 0 0 3px var(--orange); }
</style>
</head>
<body>
<div class="sheet">
  <svg class="frame" width="928" height="1200" viewBox="0 0 928 1200" aria-hidden="true">
    <rect x="0" y="122" width="536" height="16" fill="var(--green)"/>
    <polygon points="0,152 512,152 496,180 928,180 928,376 420,376 386,418 352,376 0,376" fill="var(--teal)"/>
    <polyline points="604,0 516,170 928,170" fill="none" stroke="var(--orange)" stroke-width="5"/>
    <rect x="0" y="1100" width="36" height="100" fill="var(--green)"/>
    <rect x="892" y="1100" width="36" height="100" fill="var(--green)"/>
    <rect x="0" y="1172" width="928" height="28" fill="var(--green)"/>
  </svg>

  <div class="quest-mark"><span class="dot"></span><span class="name">SUMMIT QUEST</span></div>
  <div class="partner-mark">harbour<br>lantern</div>

  <h1 class="title"><span class="big">10 TIPS</span><span class="sub">TO IMPROVE YOUR WELLBEING</span></h1>

  <div class="intro">
    <p>Yes, you will have to get off the couch and you might need to say no to burgers for lunch every day<br>but we promise we won't turn you into lycra wearing vegans with prescriptions to Glowpantry!</p>
    <p>Small changes every day can make a huge difference.</p>
  </div>

  <div class="tip" style="top:527px"><span class="num">01</span><strong>Put on your wake up grin</strong> &nbsp;- Smile and think happy thoughts – that first 90 secs has a big impact on your day. If you start the day with bad thoughts, then it compounds – simply turn up the corners of your mouth you'll start to release endorphins and serotonin, your feel-good hormones.</div>
  <div class="tip" style="top:595px"><span class="num">02</span><strong>Drink lemon and warm water first thing</strong> – and keep drinking water all day. It will cleanse your liver, you will eat less, you'll feel better and have a clearer head.</div>
  <div class="tip" style="top:645px"><span class="num">03</span><strong>Exercise</strong> – it boosts the happy chemicals in your brain. So Be Active - get your heart rate going and stretch those muscles. At the very least take the stairs. To get your endorphins surging you'll need to really heavy breathe – so walk up those stairs faster, do your house work quicker – get that heart pumping.</div>
  <div class="tip" style="top:713px"><span class="num">04</span><strong>Eat a banana</strong> – Did you ever see a depressed chimp? Bananas help to lessen feelings of stress and anxiety due to high levels of tryptophan which converts to serotonin – one of those happy hormone. The high level of potassium helps you to be more alert and will give you energy.</div>
  <div class="tip" style="top:781px"><span class="num">05</span><strong>Put on your WOW! Glasses</strong> – Go outside and Take Notice – The wind, the warmth, the cold, the trees, the blossom, the amazing sky, the moon. The world is full of things that make you go WOW, if you just slow down and Take Notice. Even better, go with a friend and Connect as well.</div>
  <div class="tip" style="top:848px"><span class="num">06</span><strong>5 fruit and veg per day</strong> – Get the fibre into to you… &nbsp;Without it you clog up, if you clog up you get grumpy and sluggish, if you get grumpy and sluggish – let's not go there! If you have trouble fitting the veges in, put them into a smoothie.</div>
  <div class="tip" style="top:916px"><span class="num">07</span><strong>Play music</strong> – it cheers you up. Create a playlist for when you need a pick-me-up. Play it in the car to and from work, doing your housework or when you're going for that brisk walk, getting out of breath and send even more happy hormones to your brain. (No, not the sad break-up playlist!)</div>
  <div class="tip" style="top:985px"><span class="num">08</span><strong>Remove a poison</strong> – Take away something that you know is bad for you – fast food, sugar, gluten – even for a couple of days a week – replace it with something healthy like water, fruit, veg, quinoa, exercise whatever works for you.</div>
  <div class="tip" style="top:1052px"><span class="num">09</span><strong>Kill em with kindness</strong> – When you're feeling bad, do something nice for someone else and it will make their day and you'll feel even better. In fact, Give every day.</div>
  <div class="tip" style="top:1101px"><span class="num">10</span><strong>Keep the cogs turning</strong> – Use it or lose it as they say – use your brain. Keep learning – something new every day.</div>
</div>
</body>
</html>
```